Norlo Tiered Food/Dessert Trays Spec Sheet

We need an elegant spec sheet template to use with our food/dessert trays. This will accompany the item when it ships out and on the web. It is something we would like to email our customers when they are considering our different banquet trays. It is important that it does not look too retail. We are the manufacturer and do not sell retail. We are business to business. It needs to help a salesman make a sale and look elegant enough while conveying the info to them.
Updates

Target Market(s)

Banquet Halls, Caterers, Country Clubs, Wedding and event centers.

Industry/Entity Type

Event

Font styles to use
Serif
Decorative
Script

Requirements
Must have
• All the copy in the word doc. Also use the model name as the heading at the top of the sheet
Nice to have
• An elegant but professional look
Should not have
• Not too busy

```html
<!DOCTYPE html>
<html lang="en">
<head>
<meta charset="utf-8">
<title>Norlo Regent Deluxe Spec Sheet</title>
<link href="https://fonts.googleapis.com/css2?family=Open+Sans:wght@400;600;700&display=swap" rel="stylesheet">
<style>
  :root {
    --page-bg: #d9d9d7;
    --sheet-top: #ffffff;
    --sheet-bottom: #dcdcdc;
    --ink: #3a3a3a;
    --ink-soft: #5a5a5a;
    --rule: #6b6b6b;
    --photo-dark: #2a1d14;
    --photo-mid: #7a5638;
    --photo-warm: #c89a6a;
    --brand-light: #ffffff;
  }
  * { margin: 0; padding: 0; box-sizing: border-box; }
  html, body {
    width: 1200px; height: 900px; overflow: hidden;
    background: var(--page-bg);
    font-family: "Open Sans", Arial, sans-serif;
    color: var(--ink);
  }
  .spec-sheet {
    position: absolute; left: 300px; top: 25px;
    width: 600px; height: 850px;
    background: linear-gradient(180deg, var(--sheet-top) 60%, var(--sheet-bottom) 100%);
    box-shadow: 0 6px 22px rgba(0,0,0,.25);
    overflow: hidden;
  }
  .hero-photo {
    position: absolute; left: 0; top: 0; width: 600px; height: 470px;
    background:
      radial-gradient(ellipse 45% 55% at 58% 52%, #e9e2d6 0%, rgba(233,226,214,.5) 35%, rgba(0,0,0,0) 70%),
      radial-gradient(ellipse 30% 25% at 12% 22%, #b87a86 0%, rgba(184,122,134,0) 100%),
      linear-gradient(180deg, var(--photo-dark) 0%, var(--photo-mid) 35%, var(--photo-warm) 70%, #e8dccd 100%);
  }
  .brand-mark {
    position: absolute; left: 26px; top: 160px;
    display: flex; align-items: center; gap: 10px;
    color: var(--brand-light);
    font-weight: 400; font-size: 26px; line-height: 1; letter-spacing: 1px;
    text-transform: uppercase;
  }
  .brand-mark .brand-square { width: 34px; height: 34px; background: var(--brand-light); }
  .brand-mark .brand-name { display: flex; flex-direction: column; gap: 4px; }
  .brand-mark .brand-name small { font-size: 14px; letter-spacing: 3px; }
  .product-intro {
    position: absolute; left: 36px; top: 490px; width: 532px;
    font-size: 11px; line-height: 1.75; color: var(--ink);
  }
  .product-intro strong { font-weight: 700; }
  .spec-columns {
    position: absolute; left: 58px; top: 600px; width: 500px;
    display: flex; justify-content: space-between;
  }
  .spec-list { list-style: none; font-size: 10px; line-height: 1.85; color: var(--ink-soft); }
  .spec-list .list-title { font-weight: 700; color: var(--ink); }
  .spec-list.product-specs { margin-top: 32px; }
  .feature-list { width: 250px; }
  .contact-rule {
    position: absolute; left: 300px; top: 776px; width: 250px;
    border-top: 1px solid var(--rule);
  }
  .contact-lines {
    position: absolute; left: 312px; top: 782px;
    font-size: 7px; line-height: 1.8; color: var(--ink-soft);
    display: grid; grid-template-columns: auto auto; column-gap: 14px;
  }
  .footer-rule {
    position: absolute; left: 48px; top: 800px; width: 220px;
    border-top: 1px solid var(--rule);
  }
  .company-name {
    position: absolute; left: 70px; top: 808px;
    font-size: 14px; color: var(--ink-soft);
  }
</style>
</head>
<body>
  <main class="spec-sheet">
    <div class="hero-photo" role="img" aria-label="Banquet table setting with flowers and candles, featuring the three-tier polished steel buffet stand"></div>
    <div class="brand-mark">
      <span class="brand-square"></span>
      <span class="brand-name">Norlo<small>Fountains</small></span>
    </div>

    <p class="product-intro"><strong>The Regent Deluxe Three-</strong>Tier Buffet Stand Features Polished, Stainless Steel, Trays and Base. It Also Features Bright Nickel Plated Silver Columns. This Eye Catching Stand with Its Large Tray Sizes Make it an Excellent Choice for Serving Large Groups at Banquets, Buffets or any Catering Operation. Create Stunning Appetizers, Finger Foods, Main Courses and More. This Stand is a True Caterers Dream...</p>

    <div class="spec-columns">
      <ul class="spec-list product-specs">
        <li class="list-title">Product Specs:</li>
        <li>Model # : RGD24-1814-S</li>
        <li>Model Name: Regent Deluxe</li>
        <li>Height: 33"</li>
        <li>Tray Sizes: 24", 18", 14"</li>
        <li>Product Weight: 20lbs</li>
        <li>Shipping Weight: 28lbs</li>
        <li>Shipping Dimensions: 27 x 27 x 10 Inches</li>
      </ul>
      <ul class="spec-list feature-list">
        <li class="list-title">Features:</li>
        <li>Designed for Repeated Commercial Use</li>
        <li>High Polished Stainless Steel Trays &amp; Base</li>
        <li>Decorative Silver Bow Tie Trim on the Base</li>
        <li>Nickel Plated Silver Columns ( No Tarnish, No Polish )</li>
        <li>Self-Serving Buffet Station</li>
        <li>No Tools Needed for Assembly or Disassembly</li>
        <li>Breaks Down for Easy Clean Up and Storage</li>
        <li>1 Year Limited Warranty</li>
      </ul>
    </div>

    <div class="contact-rule"></div>
    <div class="contact-lines">
      <span>Web: www.norlofountains.com</span><span>Phone: 800-555-0142</span>
      <span>Fax: 215-555-0178</span><span>Email: info@norlofountains.com</span>
    </div>

    <div class="footer-rule"></div>
    <p class="company-name">Norlo Fountain Sales, Inc.</p>
  </main>
</body>
</html>
```